QRV Business Cards

We are looking for innovative edits to freshen up the card we uploaded. Several examples to choose from will be very helpful. Once we get this decided we will need cards for approximately 20 people.

From the BC attached you will see most of the content we want to keep, we are looking for layout options..the Logo must stay red/blue everything else may be changed to enhance.

Each employee will have their picture on the card.

Target Market(s)

B2B and Government agencies

Industry/Entity Type

Business

Contact Information for Business Card

This is a double sided fold over business card.

Requirements
Must have
• LOGO - same color and format
• LED Lighting Solutions w/Design, Installation, Financing as a stand out
Nice to have
• We had a cartoon charter drawn but I'm not sure if he will fit the card or not...just providing an idea.

```html
<!DOCTYPE html>
<html lang="en">
<head>
<meta charset="utf-8">
<title>QRV Business Card</title>
<link rel="stylesheet" href="https://fonts.googleapis.com/css2?family=Arimo:wght@400;700&display=swap">
<style>
  :root {
    --red: #e0202e;
    --blue: #2e3a92;
    --white: #ffffff;
    --page: #ecebe8;
    --hero-a: #d9dcf0;
    --hero-b: #f3d3d5;
  }
  * { box-sizing: border-box; margin: 0; padding: 0; }
  html, body { width: 1200px; height: 848px; overflow: hidden; }
  body {
    background: var(--page);
    font-family: "Arimo", Arial, sans-serif;
    display: flex;
    flex-direction: column;
    align-items: center;
    justify-content: center;
    gap: 24px;
  }
  .card {
    width: 680px;
    height: 388px;
    background: var(--white);
    position: relative;
    overflow: hidden;
    box-shadow: 0 4px 14px rgba(0,0,0,.18);
  }
  /* Front */
  .front-top {
    height: 228px;
    display: flex;
    flex-direction: column;
    align-items: center;
    justify-content: center;
    padding-top: 12px;
  }
  .brand {
    color: var(--red);
    font-weight: 700;
    font-size: 62px;
    letter-spacing: 4px;
    line-height: 1;
  }
  .brand-sub {
    color: var(--red);
    font-weight: 700;
    font-size: 18px;
    letter-spacing: 3px;
    margin-top: 6px;
    text-transform: uppercase;
  }
  .person-name {
    color: var(--red);
    font-size: 30px;
    font-weight: 400;
    margin-top: 20px;
  }
  .person-title {
    color: var(--blue);
    font-size: 15px;
    margin-top: 2px;
  }
  .contact-band {
    height: 48px;
    background: var(--red);
    display: flex;
    align-items: center;
  }
  .contact {
    flex: 1;
    display: flex;
    align-items: center;
    justify-content: center;
    gap: 12px;
    color: var(--white);
    font-size: 21px;
    height: 100%;
  }
  .contact + .contact { border-left: 3px solid var(--white); }
  .contact svg { width: 20px; height: 20px; fill: var(--white); }
  .services {
    height: 112px;
    background: var(--blue);
    color: var(--white);
    font-size: 17px;
    line-height: 1.35;
    text-align: center;
    display: flex;
    flex-direction: column;
    justify-content: center;
    padding: 0 20px;
  }
  /* Back */
  .hero-art {
    position: absolute;
    left: 40px;
    top: 24px;
    width: 600px;
    height: 272px;
    background: linear-gradient(120deg, var(--hero-a), var(--hero-b));
  }
  .address-band {
    position: absolute;
    left: 0; right: 0; bottom: 0;
    height: 66px;
    background: var(--red);
    color: var(--white);
    font-size: 24px;
    display: flex;
    align-items: center;
    justify-content: center;
    letter-spacing: .5px;
  }
</style>
</head>
<body>
  <section class="card card-front">
    <div class="front-top">
      <div class="brand">QRV</div>
      <div class="brand-sub">Incorporated</div>
      <div class="person-name">Dana Whitcomb</div>
      <div class="person-title">Chief Executive Officer</div>
    </div>
    <div class="contact-band">
      <div class="contact">
        <svg viewBox="0 0 24 24" aria-hidden="true"><path d="M6.6 10.8a15.1 15.1 0 0 0 6.6 6.6l2.2-2.2a1 1 0 0 1 1-.25 11.4 11.4 0 0 0 3.6.57 1 1 0 0 1 1 1V20a1 1 0 0 1-1 1A17 17 0 0 1 3 4a1 1 0 0 1 1-1h3.5a1 1 0 0 1 1 1c0 1.25.2 2.45.57 3.57a1 1 0 0 1-.25 1z"/></svg>
        <span>555-014-2200</span>
      </div>
      <div class="contact">
        <svg viewBox="0 0 24 24" aria-hidden="true"><path d="M7 2h10a2 2 0 0 1 2 2v16a2 2 0 0 1-2 2H7a2 2 0 0 1-2-2V4a2 2 0 0 1 2-2zm0 3v13h10V5zm5 14.2a1 1 0 1 0 0 2 1 1 0 0 0 0-2z"/></svg>
        <span>555-016-3380</span>
      </div>
      <div class="contact">
        <svg viewBox="0 0 24 24" aria-hidden="true"><path d="M7 3h10v4H7zM4 8h16a2 2 0 0 1 2 2v6h-4v4H6v-4H2v-6a2 2 0 0 1 2-2zm4 7v3h8v-3z"/></svg>
        <span>555-014-2201</span>
      </div>
    </div>
    <div class="services">
      <p>24 Emergency Service | Directional Drilling | Electrical Services | Energy Audits</p>
      <p>Night Inspections | Parking Lot Lighting | Pole Inspections | Roadway Lighting</p>
      <p>Sign Services | Sports Lighting | Stray Voltage Testing | Traffic Signals</p>
      <p>Utility Locating | Vacuum Excavation</p>
    </div>
  </section>

  <section class="card card-back">
    <div class="hero-art" role="img" aria-label="Illustration of three flying caped mascot characters in red and blue costumes"></div>
    <div class="address-band">418 Harbor Aven., Millbrook, MD 20999</div>
  </section>
</body>
</html>
```